Bookcover: Ways to Turn Into a Bold Pathfinder

I am publishing a super-low-cost innovation book for €4,99 on Pageleaf Open Press to help everyone become a great innovator: young ambitious people without college education nor a big budget. Do you want to help me?

Brief:
Design a book cover 1600 x 2560 pixels for POP.
Main title: Ways to Turn Into a Bold Pathfinder
Sub title: mindset - insights - skills & tools
Author: Maarten de Kolkema
Design: captive, and appealing to everyone
Target Group: young ambitious people without college education

For pageleaf please format the height/width ratio of 1.6:1

```html
<!DOCTYPE html>
<html lang="en">
<head>
<meta charset="utf-8">
<title>Ways to Turn Into a Bold Pathfinder — Book Cover</title>
<link rel="stylesheet" href="https://fonts.googleapis.com/css2?family=Roboto:wght@700;900&family=Roboto+Condensed:wght@700&display=swap">
<style>
  :root {
    --navy: #15365c;
    --red: #ff2d00;
    --white: #ffffff;
    --sky: #cfe0f7;
    --sky-deep: #9dbff5;
    --sun: #f6cd7f;
    --coral: #f2775a;
  }
  html, body {
    margin: 0;
    padding: 0;
    overflow: hidden;
    background: var(--white);
  }
  .cover {
    position: relative;
    width: 750px;
    height: 1200px;
    overflow: hidden;
    background: var(--white);
    font-family: "Roboto", Arial, sans-serif;
  }
  .title-block {
    position: absolute;
    left: 0;
    top: 0;
    width: 750px;
    height: 400px;
  }
  .title-line {
    font-family: "Roboto", Arial, sans-serif;
    font-weight: 900;
    fill: var(--navy);
  }
  .title-line--accent {
    fill: var(--red);
  }
  .ribbon {
    position: absolute;
    left: 61px;
    top: 402px;
    width: 629px;
    height: 74px;
  }
  .ribbon-shape { fill: var(--navy); }
  .ribbon-text {
    font-family: "Roboto Condensed", "Arial Narrow", sans-serif;
    font-weight: 700;
    font-size: 31px;
    fill: var(--white);
  }
  .illustration {
    position: absolute;
    left: 45px;
    top: 510px;
    width: 660px;
    height: 600px;
    background:
      radial-gradient(ellipse at 30% 35%, var(--sky-deep) 0%, rgba(157,191,245,0) 45%),
      radial-gradient(ellipse at 70% 70%, var(--sun) 0%, rgba(246,205,127,0) 55%),
      radial-gradient(ellipse at 50% 90%, rgba(242,119,90,0.35) 0%, rgba(242,119,90,0) 50%),
      linear-gradient(180deg, #ffffff 0%, #f4f8fe 100%);
  }
  .author-band {
    position: absolute;
    left: 0;
    top: 1111px;
    width: 750px;
    height: 89px;
    background: var(--navy);
  }
  .author-band svg { display: block; }
  .author-name {
    font-family: "Roboto", Arial, sans-serif;
    font-weight: 700;
    font-size: 56px;
    fill: var(--white);
  }
</style>
</head>
<body>
  <main class="cover">
    <svg class="title-block" viewBox="0 0 750 400" aria-label="Ways to Turn Into a Bold Pathfinder">
      <defs>
        <linearGradient id="rule-left" x1="0" x2="1" y1="0" y2="0">
          <stop offset="0" stop-color="#15365c" stop-opacity="0"/>
          <stop offset="0.45" stop-color="#15365c" stop-opacity="1"/>
        </linearGradient>
        <linearGradient id="rule-right" x1="1" x2="0" y1="0" y2="0">
          <stop offset="0" stop-color="#15365c" stop-opacity="0"/>
          <stop offset="0.45" stop-color="#15365c" stop-opacity="1"/>
        </linearGradient>
      </defs>
      <text class="title-line" x="54" y="149" font-size="94" textLength="645" lengthAdjust="spacingAndGlyphs">WAYS TO TURN INTO</text>
      <rect x="52" y="209" width="158" height="5" fill="url(#rule-left)"/>
      <rect x="538" y="209" width="158" height="5" fill="url(#rule-right)"/>
      <text class="title-line" x="218" y="247" font-size="94" textLength="314" lengthAdjust="spacingAndGlyphs">A BOLD</text>
      <text class="title-line title-line--accent" x="54" y="376" font-size="134" textLength="646" lengthAdjust="spacingAndGlyphs">PATHFINDER</text>
    </svg>

    <svg class="ribbon" viewBox="0 0 629 74" aria-label="Mindset - Insights - Skills &amp; Tools">
      <polygon class="ribbon-shape" points="0,0 629,0 594,37 629,74 0,74 35,37"/>
      <text class="ribbon-text" x="59" y="50" textLength="510" lengthAdjust="spacingAndGlyphs">MINDSET - INSIGHTS - SKILLS &amp; TOOLS</text>
    </svg>

    <div class="illustration" role="img" aria-label="Illustration of a cheerful team around gears and a rising arrow, with one person on top holding a flag"></div>

    <footer class="author-band">
      <svg viewBox="0 0 750 89" width="750" height="89" aria-label="Maarten de Kolkema">
        <text class="author-name" x="100" y="65" textLength="550" lengthAdjust="spacingAndGlyphs">MAARTEN DE KOLKEMA</text>
      </svg>
    </footer>
  </main>
</body>
</html>
```